Skatepark, and Teenage Music/Recreation Venue needs logo, business card and letterhead. Website desi

- Logo, Letterhead & Business Card design for a new start Skatepark and Youth Venue called "The Kelp" (Pty.Ltd company) in Australia.

- Website and App design will follow within 6-months.

- Facility centered around world class skatepark which incorporates the use of innovative technology applications to enhance consumer experience, it will also provide a live entertainment & music venue for teenagers.

- Appearance should appeal to the 'mature' teenage population, the aim is provide an excellent membership experience which can be associated with the club brand.

Overall the design should communicate:
Excitement, energy, exclusivity and style

- Clean and modern fonts and styling preferred.
- Logos the I personally like: Brimlow, Corvessane, (but they don't have to be round!)
- Generally I prefer understated business cards that are subtlety/elegently distinct
- ideally the logo would be expected to standalone if no text were available. (if that makes sense?)

Business

The Kelp

```html
<!DOCTYPE html>
<html lang="en">
<head>
<meta charset="utf-8">
<title>The Kelp — Business Card</title>
<link rel="stylesheet" href="https://fonts.googleapis.com/css2?family=Arimo:wght@400;700&display=swap">
<style>
  :root {
    --page: #ffffff;
    --kelp-green: #4eb84a;
    --kelp-green-edge: #3f9a3c;
    --card-back: #e5e5e5;
    --card-back-edge: #c9c9c9;
    --ink: #1e1e1e;
  }
  * { margin: 0; padding: 0; box-sizing: border-box; }
  html, body {
    width: 1200px; height: 1067px; overflow: hidden;
    background: var(--page);
    font-family: "Arimo", Arial, sans-serif;
    color: var(--ink);
  }
  .canvas { position: relative; width: 1200px; height: 1067px; }
  .card {
    position: absolute; top: 347px; width: 510px; height: 317px;
    border-radius: 32px; overflow: hidden;
  }
  .card-front {
    left: 76px; background: var(--kelp-green);
    box-shadow: 0 3px 0 var(--kelp-green-edge), 0 4px 6px rgba(0,0,0,.25);
    display: flex; align-items: center; justify-content: center;
  }
  .brand-name {
    font-weight: 700; font-size: 46px; letter-spacing: 1px;
    color: var(--ink);
  }
  .card-back {
    left: 615px; background: var(--card-back);
    box-shadow: 0 3px 0 var(--card-back-edge), 0 4px 6px rgba(0,0,0,.2);
  }
  .contact-band {
    position: absolute; left: 0; top: 142px; width: 98px; height: 148px;
    background: var(--kelp-green);
  }
  .icon {
    position: absolute; left: 72px; width: 17px; height: 17px;
    background: var(--ink); border-radius: 4px;
    display: flex; align-items: center; justify-content: center;
  }
  .icon svg { width: 11px; height: 11px; fill: #fff; }
  .holder-name {
    position: absolute; left: 122px; top: 93px;
    font-size: 27px; font-weight: 700;
  }
  .line {
    position: absolute; left: 122px; font-size: 19px; line-height: 23px;
  }
</style>
</head>
<body>
<main class="canvas">
  <section class="card card-front">
    <span class="brand-name">THE KELP</span>
  </section>

  <section class="card card-back">
    <div class="contact-band"></div>

    <span class="icon" style="top:157px">
      <svg viewBox="0 0 12 12"><path d="M6 1 1 5.5h1.5V11h3V8h1v3h3V5.5H11z"/></svg>
    </span>
    <span class="icon" style="top:210px">
      <svg viewBox="0 0 12 12"><path d="M2.5 1h2l1 3-1.3 1a6 6 0 0 0 2.8 2.8l1-1.3 3 1v2c0 .6-.5 1.5-1.5 1.5A9.5 9.5 0 0 1 1 2.5C1 1.5 1.9 1 2.5 1z"/></svg>
    </span>
    <span class="icon" style="top:239px">
      <svg viewBox="0 0 12 12"><path d="M1 3h10v6H1z M1 3l5 3.5L11 3" stroke="#1e1e1e" stroke-width=".8"/></svg>
    </span>
    <span class="icon" style="top:267px">
      <svg viewBox="0 0 12 12"><circle cx="6" cy="6" r="5" fill="none" stroke="#fff" stroke-width="1"/><path d="M1 6h10M6 1v10" stroke="#fff" stroke-width=".8"/><ellipse cx="6" cy="6" rx="2.3" ry="5" fill="none" stroke="#fff" stroke-width=".8"/></svg>
    </span>

    <h1 class="holder-name">Your name</h1>
    <p class="line" style="top:140px">412 Marrow road shopping centre<br>Tallen, Queen land 4571</p>
    <p class="line" style="top:195px">955 - 010 - 2468<br>955 - 010 - 2468</p>
    <p class="line" style="top:241px">thekelp@mailbox.com</p>
    <p class="line" style="top:267px">thekelporggroup.com</p>
  </section>
</main>
</body>
</html>
```